Vacation giveaway landing page design

We are giving away a holiday/vacation to Rome and we need a landing page designed that will entice people to enter their email address for a chance to win!

Full brief, examples and everything else can be found in this document: https://files.brintowle.net/papers/p/4-wxkoppTR7mnbQ2vyLazcR5xsjfPe3lhmwcKt27r/view?mode=linked

1 page

```html
<!DOCTYPE html>
<html lang="en">
<head>
<meta charset="utf-8">
<title>Wander Lot – Win a Holiday in Rome</title>
<link rel="stylesheet" href="https://fonts.googleapis.com/css2?family=Nunito:wght@700;800&family=Barlow+Semi+Condensed:wght@400;500;600&family=Dancing+Script:wght@400&display=swap">
<style>
:root{
  --teal:#37c4bd;
  --teal-dark:#1f6f6a;
  --yellow:#f2c12e;
  --ink:#3a3a3a;
  --muted:#8a8a8a;
  --white:#ffffff;
  --heart:#e8433f;
  --stone-light:#f0d3b6;
  --stone-dark:#c99168;
}
*{box-sizing:border-box;margin:0;padding:0}
html,body{width:1012px;height:1200px;overflow:hidden;background:var(--white)}
body{position:relative;font-family:"Barlow Semi Condensed",Arial,sans-serif;color:var(--ink)}
.abs{position:absolute}
ul{list-style:none}

/* hero */
.hero{position:absolute;left:38px;top:38px;width:974px;height:531px;background:var(--teal);border-radius:6px 0 0 6px;overflow:hidden}
.hero-photo{position:absolute;left:520px;top:44px;width:454px;height:487px;border-radius:10px 0 0 0;background:linear-gradient(180deg,var(--stone-dark) 0%,#dcab82 50%,var(--stone-light) 100%)}
.brand{position:absolute;display:flex;align-items:center;gap:7px;font-family:"Nunito",sans-serif;font-weight:800;letter-spacing:.5px}
.brand-dot{width:26px;height:26px;border-radius:50%;border:2px solid currentColor}
.hero .brand{left:98px;top:38px;color:var(--white);font-size:19px}
.script{font-family:"Dancing Script",cursive;font-weight:400}
.hero-kicker{left:98px;top:118px;font-size:17px;color:rgba(255,255,255,.55)}
.hero-lead{left:98px;top:147px;font-family:"Nunito",sans-serif;font-weight:700;font-size:19px;color:var(--white)}
.hero-title{left:98px;top:170px;font-family:"Nunito",sans-serif;font-weight:800;font-size:37px;color:var(--white);letter-spacing:-.3px}
.hero-copy{left:98px;top:231px;width:258px;font-size:11.5px;line-height:16.5px;color:var(--white);font-weight:500}
.hero-copy b{font-weight:600}
.perks{left:98px;top:276px;display:flex;gap:10px}
.perk{height:22px;padding:0 12px;border-radius:11px;background:rgba(255,255,255,.18);display:flex;align-items:center;gap:5px;color:var(--white);font-size:11.5px;font-weight:500;letter-spacing:.2px}
.perk svg{width:10px;height:10px}
.stars{color:var(--yellow);letter-spacing:3px;font-size:11px;margin-left:4px}
.field-label{display:flex;align-items:center;gap:6px;color:var(--white);font-size:11.5px;font-weight:500;letter-spacing:.4px}
.field-label svg{width:12px;height:10px}
.hero .field-label{position:absolute;left:98px;top:318px}
.email-input{position:absolute;background:var(--white);border-radius:2px;display:flex;align-items:center;padding-left:13px;font-size:9px;letter-spacing:.4px;color:#c8c8c8}
.cta{position:absolute;background:var(--yellow);border-radius:2px;display:flex;align-items:center;justify-content:center;color:var(--white);font-size:12px;font-weight:500;letter-spacing:.4px}
.hero .email-input{left:98px;top:341px;width:196px;height:31px}
.hero .cta{left:98px;top:385px;width:196px;height:38px}
.hero-terms{left:98px;top:440px;width:255px;font-size:9.3px;line-height:17.6px;color:var(--white);font-weight:500}

/* winners */
.winners-title{left:0;top:618px;width:1012px;text-align:center;font-family:"Nunito",sans-serif;font-weight:800;font-size:22px;color:var(--ink)}
.winner{position:absolute;top:727px;width:234px;height:139px;border:1.3px solid var(--teal);border-radius:2px}
.winner-photo{position:absolute;left:21px;top:-34px;width:70px;height:70px;border-radius:50%}
.winner-month{position:absolute;left:96px;top:11px;font-size:10px;color:var(--teal)}
.winner-name{position:absolute;left:96px;top:25px;font-family:"Nunito",sans-serif;font-weight:800;font-size:12px;color:var(--teal-dark)}
.winner-text{position:absolute;left:12px;top:57px;width:176px;font-size:10px;line-height:16.5px;color:var(--ink)}
.winner-text span{color:var(--muted)}
.winner-rule{position:absolute;left:12px;right:12px;top:108px;border-top:1px solid #e4e4e4}
.winner-stats{position:absolute;left:12px;top:117px;display:flex;gap:13px;font-size:9.5px;color:#b4b4b4}
.stat{display:flex;align-items:center;gap:5px}
.stat svg{width:9px;height:9px;fill:#c4c4c4}
.stat.liked{color:var(--heart)}
.stat.liked svg{fill:var(--heart)}
.arrow{position:absolute;top:785px;width:12px;height:22px}
.dots{left:0;top:897px;width:1012px;display:flex;justify-content:center;gap:8px;padding-left:18px}
.dots i{width:4px;height:4px;border-radius:50%;background:#d6d6d6}
.dots i.on{width:5px;height:5px;background:var(--teal)}

/* closing band */
.signup-band{position:absolute;left:0;top:975px;width:974px;height:158px;background:var(--teal);border-radius:0 8px 8px 0;overflow:hidden}
.band-photo{position:absolute;left:300px;top:0;width:674px;height:158px;background:linear-gradient(100deg,rgba(55,196,189,1) 0%,rgba(55,196,189,.2) 12%,#2a8f86 40%,#1f6b62 70%,#3aa89c 100%);clip-path:polygon(10% 100%,18% 45%,32% 12%,45% 0,100% 0,100% 100%)}
.band-kicker{left:136px;top:1029px;font-size:15px;color:var(--white)}
.band-title{left:136px;top:1049px;font-family:"Nunito",sans-serif;font-weight:800;font-size:26px;color:var(--white)}
.band-label{position:absolute;left:536px;top:1026px}
.band-input{left:536px;top:1047px;width:195px;height:31px}
.band-cta{left:749px;top:1047px;width:127px;height:31px}

/* footer */
.site-footer .brand{left:136px;top:1152px;color:var(--teal);font-size:17px}
.copyright{left:0;width:876px;text-align:right;top:1159px;font-size:10px;color:var(--ink)}
</style>
</head>
<body>

<section class="hero">
  <div class="hero-photo" role="img" aria-label="Photo of a dome and rooftops in Rome, tinted in warm stone tones"></div>

  <div class="brand"><span class="brand-dot"></span>Wander Lot</div>
  <p class="abs hero-kicker script">Always had dreams to visit Rome?</p>
  <p class="abs hero-lead">Your next Holiday could be in</p>
  <h1 class="abs hero-title">The Eternal City</h1>
  <p class="abs hero-copy">Enter your email to have a chance to win a <b>FREE</b> holiday in Rome that include:</p>

  <ul class="abs perks">
    <li class="perk"><svg viewBox="0 0 10 10"><path d="M1 5.5 L4 8 L9 2" fill="none" stroke="#f2c12e" stroke-width="1.4"/></svg>4 NIGHTS FOR 2 PEOPLE</li>
    <li class="perk"><svg viewBox="0 0 10 10"><path d="M1 5.5 L4 8 L9 2" fill="none" stroke="#f2c12e" stroke-width="1.4"/></svg>FLIGHTS</li>
    <li class="perk"><svg viewBox="0 0 10 10"><path d="M1 5.5 L4 8 L9 2" fill="none" stroke="#f2c12e" stroke-width="1.4"/></svg>HOTEL<span class="stars">★★★★</span></li>
  </ul>

  <label class="field-label"><svg viewBox="0 0 12 10"><rect x=".6" y=".6" width="10.8" height="8.8" rx="1" fill="none" stroke="#fff" stroke-width="1.1"/><path d="M1 1.5 L6 5.5 L11 1.5" fill="none" stroke="#fff" stroke-width="1.1"/></svg>EMAIL ADDRESS</label>
  <div class="email-input">YOUR FANCY EMAIL</div>
  <div class="cta">ENTER NOW</div>
  <p class="abs hero-terms">By entering your email address, you agree to receive updates about the competition and Wander Lot. You can review our competition terms and conditions Here</p>
</section>

<h2 class="abs winners-title">See our previous winners</h2>

<svg class="arrow" style="left:106px" viewBox="0 0 12 22"><path d="M11 1 L1 11 L11 21" fill="none" stroke="#cfcfcf" stroke-width="1.3"/></svg>
<svg class="arrow" style="left:894px" viewBox="0 0 12 22"><path d="M1 1 L11 11 L1 21" fill="none" stroke="#37c4bd" stroke-width="1.3"/></svg>

<article class="winner" style="left:136px">
  <div class="winner-photo" role="img" aria-label="Photo of the November winner with a friend" style="background:radial-gradient(circle at 45% 40%,#d8b49a,#6d5a4d 70%)"></div>
  <p class="winner-month">November's Winner</p>
  <h3 class="winner-name">Mia Calloway</h3>
  <p class="winner-text">Congrats to this month's winner - Mia Calloway <span>Read more</span></p>
  <div class="winner-rule"></div>
  <div class="winner-stats">
    <span class="stat liked"><svg viewBox="0 0 10 10"><path d="M5 9 L1 5 A2.2 2.2 0 0 1 5 2 A2.2 2.2 0 0 1 9 5 Z"/></svg>25</span>
    <span class="stat"><svg viewBox="0 0 10 10"><path d="M5 1 A4 3.5 0 1 1 3 8 L1 9 L2 7 A4 3.5 0 0 1 5 1 Z"/></svg>12</span>
    <span class="stat"><svg viewBox="0 0 10 10"><path d="M6 1 L10 4.5 L6 8 V6 C3 6 1.5 7 0.5 9 C1 5.5 3 3.5 6 3.2 Z"/></svg>8</span>
  </div>
</article>

<article class="winner" style="left:389px">
  <div class="winner-photo" role="img" aria-label="Photo of the December winner" style="background:radial-gradient(circle at 50% 45%,#d9a98a,#5a2b55 70%)"></div>
  <p class="winner-month">December's Winner</p>
  <h3 class="winner-name">Jess Harlow</h3>
  <p class="winner-text">Congrats to this month's winner - Mia Calloway <span>Read more</span></p>
  <div class="winner-rule"></div>
  <div class="winner-stats">
    <span class="stat"><svg viewBox="0 0 10 10"><path d="M5 9 L1 5 A2.2 2.2 0 0 1 5 2 A2.2 2.2 0 0 1 9 5 Z"/></svg>45</span>
    <span class="stat"><svg viewBox="0 0 10 10"><path d="M5 1 A4 3.5 0 1 1 3 8 L1 9 L2 7 A4 3.5 0 0 1 5 1 Z"/></svg>22</span>
    <span class="stat"><svg viewBox="0 0 10 10"><path d="M6 1 L10 4.5 L6 8 V6 C3 6 1.5 7 0.5 9 C1 5.5 3 3.5 6 3.2 Z"/></svg>17</span>
  </div>
</article>

<article class="winner" style="left:642px">
  <div class="winner-photo" role="img" aria-label="Photo of the January winner on a city street" style="background:radial-gradient(circle at 55% 45%,#a67e68,#2d2a2c 70%)"></div>
  <p class="winner-month">January's Winner</p>
  <h3 class="winner-name">Nadia Rehan</h3>
  <p class="winner-text">Congrats to this month's winner - Mia Calloway <span>Read more</span></p>
  <div class="winner-rule"></div>
  <div class="winner-stats">
    <span class="stat"><svg viewBox="0 0 10 10"><path d="M5 9 L1 5 A2.2 2.2 0 0 1 5 2 A2.2 2.2 0 0 1 9 5 Z"/></svg>124</span>
    <span class="stat"><svg viewBox="0 0 10 10"><path d="M5 1 A4 3.5 0 1 1 3 8 L1 9 L2 7 A4 3.5 0 0 1 5 1 Z"/></svg>62</span>
    <span class="stat"><svg viewBox="0 0 10 10"><path d="M6 1 L10 4.5 L6 8 V6 C3 6 1.5 7 0.5 9 C1 5.5 3 3.5 6 3.2 Z"/></svg>27</span>
  </div>
</article>

<div class="abs dots"><i class="on"></i><i></i><i></i><i></i><i></i></div>

<section class="signup-band">
  <div class="band-photo" role="img" aria-label="Teal-tinted photo of the Colosseum arches"></div>
</section>
<p class="abs band-kicker script">Enter the Giveaway now!</p>
<h2 class="abs band-title">Save your spot now!</h2>
<label class="field-label band-label"><svg viewBox="0 0 12 10"><rect x=".6" y=".6" width="10.8" height="8.8" rx="1" fill="none" stroke="#fff" stroke-width="1.1"/><path d="M1 1.5 L6 5.5 L11 1.5" fill="none" stroke="#fff" stroke-width="1.1"/></svg>EMAIL ADDRESS</label>
<div class="email-input band-input">YOUR FANCY EMAIL</div>
<div class="cta band-cta">ENTER NOW</div>

<footer class="site-footer">
  <div class="brand"><span class="brand-dot"></span>Wander Lot</div>
  <p class="abs copyright">© Copyright 2019 Wander Lot. All rights reserved</p>
</footer>

</body>
</html>
```